Organic Food company needs a new design label logo

Our company name is Brackenmoor Organic. We pack organic dried products and sell to natural, organic or small supermarkets in the UK.

We would like to you to design our new label with logo.

The label size should be the width is 65 mm and the length is 85 mm. The label should also include our tillbrook council and European organic logos.

The food label should reflect our company that we are organic and we sell quality organic food products.

The colours should be pastel and warm colour. It shouldn’t have so many colour.

Dear All,

Just let you know that this project is food label with the new design. The size of the label should as follow; 
width: 65 mm
length: 85 mm

It will be used for dried fruit, vegetables and nuts. so the middle of the label should be blank, as the print shop will print the name separetly.

When you design our new logo label, please also read my previous note.

Thank you.

Target Market(s)

Above 25 years old. People who like to buy organic or natural food products. Middle income people.

Industry/Entity Type

It Company

Requirements
Must have
• 1) Tillbrook Council logo (attached as file )

2) European organic logo ( can be download from http://ab.quorvanet.org/farming/green/mark-policy/badge_en )

3) The following information should be either next to or underneath to European logo;
GB-TRV-38
Non-EU Agriculture

The above text information shouldn't be very big.

4) There should be enough space in the middle of the label to write (later by the print shop) full product name and weight.

5) Our company name is "Brackenmoor Organic"

6) Our web site address is www.brackenmoor.com

```html
<!DOCTYPE html>
<html lang="en">
<head>
<meta charset="utf-8">
<title>Brackenmoor Organic – Product Labels</title>
<link rel="stylesheet" href="https://fonts.googleapis.com/css2?family=Bebas+Neue&family=Handlee&family=Open+Sans:wght@400;600&display=swap">
<style>
  :root {
    --canvas: #f4f3f1;
    --label-vegetable: #7b3d31;
    --label-fruit: #4b2b25;
    --label-nuts: #a9654b;
    --brand-yellow: #f6b730;
    --brand-green: #a9d13c;
    --text-light: #f3e6dc;
    --eu-green: #8fc33a;
  }
  * { margin: 0; padding: 0; box-sizing: border-box; }
  html, body {
    width: 1200px; height: 586px; overflow: hidden;
    background: var(--canvas);
  }
  .label-range {
    position: relative; width: 1200px; height: 586px;
    display: flex; justify-content: center; align-items: center; gap: 70px;
  }
  .label {
    position: relative; width: 260px; height: 340px;
    border-radius: 12px;
    font-family: "Open Sans", sans-serif;
    color: var(--text-light);
  }
  .label--vegetable { background: var(--label-vegetable); }
  .label--fruit { background: var(--label-fruit); }
  .label--nuts { background: var(--label-nuts); }

  .label__weight {
    position: absolute; top: 16px; right: 20px;
    font-size: 10px; font-family: Georgia, serif;
  }
  .label__badge {
    position: absolute; top: 24px; left: 50%; transform: translateX(-50%);
    width: 58px; height: 58px;
  }
  .brand {
    position: absolute; top: 112px; left: 0; right: 0;
    text-align: center; font-family: "Bebas Neue", sans-serif;
    color: var(--brand-yellow); line-height: 0.9;
  }
  .brand__line1 { display: block; font-size: 36px; letter-spacing: 0.5px; }
  .brand__line2 { display: block; font-size: 50px; letter-spacing: 0.5px; }
  .label__product {
    position: absolute; top: 222px; left: 0; right: 0;
    text-align: center; font-family: "Handlee", cursive; font-size: 13px;
  }
  .label__certs {
    position: absolute; left: 14px; bottom: 16px;
    display: flex; align-items: flex-end; gap: 8px;
  }
  .eu-mark { display: flex; flex-direction: column; align-items: flex-start; }
  .eu-mark__square { width: 34px; height: 23px; background: var(--eu-green); }
  .eu-mark__code { font-size: 7px; line-height: 1.1; margin-top: 2px; }
  .eu-mark__origin { font-size: 4.5px; line-height: 1.1; }
  .council-mark { width: 34px; height: 34px; }
  .label__web {
    position: absolute; right: 18px; bottom: 30px;
    font-size: 10px; color: var(--brand-green);
  }
</style>
</head>
<body>
<main class="label-range">

  <article class="label label--vegetable">
    <span class="label__weight">150gm</span>
    <svg class="label__badge" viewBox="0 0 58 58" role="img" aria-label="Premium organic products badge">
      <circle cx="29" cy="29" r="26" fill="none" stroke="var(--brand-green)" stroke-width="2"/>
    </svg>
    <h1 class="brand"><span class="brand__line1">Brackenmoor</span><span class="brand__line2">Organic</span></h1>
    <p class="label__product">Vegetable</p>
    <div class="label__certs">
      <div class="eu-mark">
        <span class="eu-mark__square" role="img" aria-label="European organic mark"></span>
        <span class="eu-mark__code">GB-TRV-38</span>
        <span class="eu-mark__origin">Non-EU Agriculture</span>
      </div>
      <svg class="council-mark" viewBox="0 0 34 34" role="img" aria-label="Tillbrook Council organic mark">
        <circle cx="17" cy="17" r="15" fill="none" stroke="var(--text-light)" stroke-width="1.5"/>
      </svg>
    </div>
    <span class="label__web">www.brackenmoor.com</span>
  </article>

  <article class="label label--fruit">
    <span class="label__weight">150gm</span>
    <svg class="label__badge" viewBox="0 0 58 58" role="img" aria-label="Premium organic products badge">
      <circle cx="29" cy="29" r="26" fill="none" stroke="var(--brand-green)" stroke-width="2"/>
    </svg>
    <h1 class="brand"><span class="brand__line1">Brackenmoor</span><span class="brand__line2">Organic</span></h1>
    <p class="label__product">Dried Fruit</p>
    <div class="label__certs">
      <div class="eu-mark">
        <span class="eu-mark__square" role="img" aria-label="European organic mark"></span>
        <span class="eu-mark__code">GB-TRV-38</span>
        <span class="eu-mark__origin">Non-EU Agriculture</span>
      </div>
      <svg class="council-mark" viewBox="0 0 34 34" role="img" aria-label="Tillbrook Council organic mark">
        <circle cx="17" cy="17" r="15" fill="none" stroke="var(--text-light)" stroke-width="1.5"/>
      </svg>
    </div>
    <span class="label__web">www.brackenmoor.com</span>
  </article>

  <article class="label label--nuts">
    <span class="label__weight">150gm</span>
    <svg class="label__badge" viewBox="0 0 58 58" role="img" aria-label="Premium organic products badge">
      <circle cx="29" cy="29" r="26" fill="none" stroke="var(--brand-green)" stroke-width="2"/>
    </svg>
    <h1 class="brand"><span class="brand__line1">Brackenmoor</span><span class="brand__line2">Organic</span></h1>
    <p class="label__product">Nuts</p>
    <div class="label__certs">
      <div class="eu-mark">
        <span class="eu-mark__square" role="img" aria-label="European organic mark"></span>
        <span class="eu-mark__code">GB-TRV-38</span>
        <span class="eu-mark__origin">Non-EU Agriculture</span>
      </div>
      <svg class="council-mark" viewBox="0 0 34 34" role="img" aria-label="Tillbrook Council organic mark">
        <circle cx="17" cy="17" r="15" fill="none" stroke="var(--text-light)" stroke-width="1.5"/>
      </svg>
    </div>
    <span class="label__web">www.brackenmoor.com</span>
  </article>

</main>
</body>
</html>
```